GoodsHarbor Capabilities Deck - Build Powerpoint Template

Hello - we need to build a capabilities deck to send to potential buyers. We have the information and need a deck built that reflects our logo and design language. We should be able to edit the powerpoint as needed and updates are required.

Target Market(s)

Marketing Teams, Sales Development Teams, HR - anyone who needs swag/merch

Font styles to use
Serif
Sans Serif

Colors
0054AA
0677BA
7BADD7
CADEEF
E8F1F8

Requirements
Must have
• Clean design reflecting our logo and highlighting our merch
Should not have
• avoid word-heavy slides, obvious AI-designs

```html
<!DOCTYPE html>
<html lang="en">
<head>
<meta charset="utf-8">
<title>GoodsHarbor Capabilities Deck</title>
<link href="https://fonts.googleapis.com/css2?family=Roboto:wght@400;500;700;900&display=swap" rel="stylesheet">
<style>
:root{
  --ink-bg:#1f1f1f;
  --blue:#0a47a6;
  --blue-deep:#083a8f;
  --blue-mid:#0677ba;
  --blue-soft:#7badd7;
  --blue-pale:#cadeef;
  --blue-wash:#e8f1f8;
  --text:#3d3f45;
  --white:#ffffff;
}
*{margin:0;padding:0;box-sizing:border-box}
html,body{width:1029px;height:1200px;overflow:hidden;background:var(--ink-bg);font-family:'Roboto',sans-serif}
.canvas{position:relative;width:1029px;height:1200px}
.slide{position:absolute;width:458px;height:258px;background:var(--white);overflow:hidden}
.col-l{left:39px}.col-r{left:533px}
.row1{top:41px}.row2{top:328px}.row3{top:614px}.row4{top:901px}

.slide-header{position:absolute;left:0;top:0;width:100%;height:30px}
.slide-header svg{position:absolute;left:0;top:0}
.slide-title{position:absolute;left:23px;top:7px;color:var(--white);font-size:13px;font-weight:400;letter-spacing:.2px}
.slide-title b{font-weight:900}

.slide-footer{position:absolute;left:0;bottom:0;width:100%;height:21px;color:var(--white);font-size:6.6px;font-weight:500}
.slide-footer svg.band{position:absolute;left:0;top:0}
.contact{position:absolute;top:7px;display:flex;align-items:center;gap:5px}
.contact i{display:block;width:6px;height:6px;background:var(--white);border-radius:1px}
.contact i.round{border-radius:50%}
.page-no{position:absolute;right:24px;top:7px}

.body-copy{font-size:7.2px;color:var(--text);line-height:14.5px;text-align:justify}
.body-copy p+p{margin-top:14.5px}

.photo{position:absolute;border-radius:14px}

/* cover */
.cover{background:linear-gradient(135deg,#0b3f9c,#0a4fb4 50%,#0a3d93)}
.cover-photo{position:absolute;left:0;top:0;width:100%;height:100%;background:radial-gradient(ellipse at 45% 45%,rgba(140,170,210,.45),rgba(10,70,170,0) 60%)}
.wordmark{display:flex;align-items:center;gap:7px;color:var(--white);font-weight:500}
.cover .wordmark{position:absolute;left:0;right:0;justify-content:center;top:215px;font-size:20px}
.wordmark .dot{width:14px;height:14px;border-radius:50%;background:var(--white)}

/* cards */
.card{position:absolute;width:94px;border-radius:9px;text-align:center}
.process .card{top:72px;height:128px;background:var(--white);box-shadow:0 2px 8px rgba(20,50,110,.14);border:1px solid #eef1f6}
.card .icon{position:absolute;left:50%;transform:translateX(-50%);border-radius:50%;background:var(--blue);display:flex;align-items:center;justify-content:center}
.process .icon{top:16px;width:31px;height:31px}
.card h3{color:var(--blue);font-weight:500;position:absolute;left:4px;right:4px}
.process h3{top:56px;font-size:8.2px}
.card p{position:absolute;left:8px;right:8px;color:var(--text)}
.process p{top:71px;font-size:6.4px;line-height:10.8px}

.why .card{background:var(--blue-wash);height:114px}
.why .icon{width:41px;height:41px;top:-20px}
.why h3{top:29px;font-size:6.2px;font-weight:700;line-height:9px}
.why p{top:45px;font-size:5.5px;line-height:9.8px;left:7px;right:7px}
.why p.two{top:54px}

/* industries */
.pill{position:absolute;width:199px;height:57px;border-radius:29px;background:var(--blue-wash);border:1px solid var(--blue-mid)}
.pill .icon{position:absolute;left:5px;top:5px;width:46px;height:46px;border-radius:50%;background:var(--blue);display:flex;align-items:center;justify-content:center}
.pill h4{position:absolute;left:60px;right:8px;color:var(--blue);font-size:6.2px;font-weight:700}
.pill p{position:absolute;left:60px;right:10px;color:var(--text);font-size:6.2px;line-height:9.8px}

/* interview */
.interview-title{position:absolute;left:24px;top:22px;color:var(--blue);font-size:13px;line-height:17px;letter-spacing:.2px}
.interview-title b{font-weight:900}
.interview-rule{position:absolute;left:153px;top:20px;width:1px;height:82px;background:#c9ccd3}
.interview-copy{position:absolute;left:170px;top:17px;width:264px;font-size:7px;line-height:12.6px;color:var(--text);text-align:justify}
.interview-photo{position:absolute;left:8px;top:124px;width:450px;height:134px;border-radius:34px 34px 0 0;background:linear-gradient(180deg,#dfe2e6,#b9b2a8 55%,#5b5450)}
.badge-ring{position:absolute;left:24px;top:101px;width:46px;height:46px;border-radius:50%;background:rgba(123,173,215,.55);display:flex;align-items:center;justify-content:center}
.badge-ring span{width:32px;height:32px;border-radius:50%;background:var(--blue);display:flex;align-items:center;justify-content:center}

/* closing */
.closing-photo{position:absolute;inset:0;background:linear-gradient(180deg,#3a3d43,#7d8085 30%,#2b2c31 70%,#5b4a3f)}
.closing-band{position:absolute;left:0;top:94px;width:100%;height:92px;background:var(--blue)}
.closing-lead{position:absolute;left:24px;top:130px;color:var(--white);font-size:12px;letter-spacing:.2px}
.closing-main{position:absolute;left:24px;top:146px;color:var(--white);font-size:18.5px;font-weight:900;letter-spacing:.4px}
.closing-rule{position:absolute;left:242px;top:121px;width:1px;height:55px;background:var(--white)}
.closing .wordmark{position:absolute;left:290px;top:148px;font-size:18px}
.chat-badge{position:absolute;left:32px;top:76px;width:34px;height:34px;border-radius:50%;background:var(--white);box-shadow:0 0 0 5px rgba(255,255,255,.25);display:flex;align-items:center;justify-content:center}
</style>
</head>
<body>
<div class="canvas">

<!-- Page 1 cover -->
<section class="slide cover col-l row1">
  <div class="cover-photo" role="img" aria-label="Blue-toned photo of a business team silhouetted against a bright window"></div>
  <div class="wordmark"><span class="dot"></span>GoodsHarbor</div>
</section>

<!-- Page 2 who we are -->
<section class="slide col-l row2">
  <div class="slide-header">
    <svg width="458" height="30"><rect x="0" y="0" width="458" height="2" fill="var(--blue)"/><polygon points="0,0 294,0 277,29 0,29" fill="var(--blue)"/></svg>
    <div class="slide-title">WHO <b>WE ARE</b></div>
  </div>
  <div class="photo" style="left:23px;top:51px;width:180px;height:160px;background:linear-gradient(160deg,#9aa3ab,#5f6a72 50%,#2f3338);box-shadow:0 2px 6px rgba(0,0,0,.2)" role="img" aria-label="Photo of four colleagues talking outside an office building"></div>
  <div class="body-copy" style="position:absolute;left:229px;top:50px;width:206px">
    <p>GoodsHarbor partners with brands and nonprofits to design, produce, and manage impactful merchandise programs that build engagement, raise awareness, and drive revenue.</p>
    <p>We work with clients across corporate, nonprofit, and entertainment sectors transforming their vision into tangible, memorable products that resonate with their audiences.</p>
    <p>We are two Retail &amp; Data Executives with a combined 25 years experience looking to streamline and perfect the merch experience.</p>
  </div>
  <footer class="slide-footer">
    <svg class="band" width="458" height="21"><rect width="458" height="21" fill="var(--blue)"/><polygon points="361,0 458,0 458,21 353,21" fill="var(--blue-deep)"/><line x1="361" y1="0" x2="353" y2="21" stroke="#fff" stroke-width="1.2"/></svg>
    <span class="contact" style="left:24px"><i></i>+1 555 014 2290</span>
    <span class="contact" style="left:116px"><i></i>HELLO@GOODSHARBOR.CO</span>
    <span class="contact" style="left:236px"><i class="round"></i>WWW.GOODSHARBOR.CO</span>
    <span class="page-no">PAGE 02 OF 08</span>
  </footer>
</section>

<!-- Page 3 process -->
<section class="slide process col-l row3">
  <div class="slide-header">
    <svg width="458" height="30"><rect x="0" y="0" width="458" height="2" fill="var(--blue)"/><polygon points="0,0 294,0 277,29 0,29" fill="var(--blue)"/></svg>
    <div class="slide-title">OUR <b>PROCESS</b></div>
  </div>
  <div class="card" style="left:23px"><div class="icon"><svg width="16" height="16" viewBox="0 0 16 16"><circle cx="8" cy="8" r="7" fill="#fff"/><path d="M4.6 8.2l2.3 2.2 4.4-4.6" stroke="var(--blue)" stroke-width="1.8" fill="none"/></svg></div><h3>DISCOVER</h3><p>Understand your brand, goals and audience through collaborative consultation</p></div>
  <div class="card" style="left:128px"><div class="icon"><svg width="16" height="16" viewBox="0 0 16 16"><circle cx="8" cy="8" r="7" fill="#fff"/><path d="M4.6 8.2l2.3 2.2 4.4-4.6" stroke="var(--blue)" stroke-width="1.8" fill="none"/></svg></div><h3>DESIGN</h3><p>Create visuals and product concepts that authentically tell your story</p></div>
  <div class="card" style="left:233px"><div class="icon"><svg width="16" height="16" viewBox="0 0 16 16"><circle cx="8" cy="8" r="7" fill="#fff"/><path d="M4.6 8.2l2.3 2.2 4.4-4.6" stroke="var(--blue)" stroke-width="1.8" fill="none"/></svg></div><h3>PRODUCE</h3><p>Manage sourcing, decoration and rigorous quality control</p></div>
  <div class="card" style="left:338px"><div class="icon"><svg width="16" height="16" viewBox="0 0 16 16"><circle cx="8" cy="8" r="7" fill="#fff"/><path d="M4.6 8.2l2.3 2.2 4.4-4.6" stroke="var(--blue)" stroke-width="1.8" fill="none"/></svg></div><h3>DELIVER</h3><p>Handle fulfillment, shipping and logistics globally with precision</p></div>
  <footer class="slide-footer">
    <svg class="band" width="458" height="21"><rect width="458" height="21" fill="var(--blue)"/><polygon points="361,0 458,0 458,21 353,21" fill="var(--blue-deep)"/><line x1="361" y1="0" x2="353" y2="21" stroke="#fff" stroke-width="1.2"/></svg>
    <span class="contact" style="left:24px"><i></i>+1 555 014 2290</span>
    <span class="contact" style="left:116px"><i></i>HELLO@GOODSHARBOR.CO</span>
    <span class="contact" style="left:236px"><i class="round"></i>WWW.GOODSHARBOR.CO</span>
    <span class="page-no">PAGE 03 OF 08</span>
  </footer>
</section>

<!-- Page 4 case study -->
<section class="slide col-l row4">
  <div class="slide-header">
    <svg width="458" height="30"><rect x="0" y="0" width="458" height="2" fill="var(--blue)"/><polygon points="0,0 294,0 277,29 0,29" fill="var(--blue)"/></svg>
    <div class="slide-title">HARMON SOUND <b>GROUP</b></div>
  </div>
  <div class="body-copy" style="position:absolute;left:23px;top:51px;width:206px">
    <p>HSG partnered with GoodsHarbor to develop custom, high-quality merchandise that reflected the individuality of its artists and elevated fan engagement.</p>
    <p>With overlapping launch timelines and rapid production needs, Harmon required a reliable creative partner who could deliver quickly without sacrificing brand integrity. GoodsHarbor managed design, sourcing, and fulfillment for apparel, accessories, and event merch - including limited-edition drops and influencer kits - ensuring on-brand, retail-quality products that deepened fan connection and amplified artist visibility.</p>
  </div>
  <div class="photo" style="left:250px;top:51px;width:180px;height:160px;background:linear-gradient(135deg,#efe9ea,#cfc6c8 40%,#3b3234);box-shadow:0 2px 6px rgba(0,0,0,.15)" role="img" aria-label="Sticker sheet merchandise with dark figure cut-outs"></div>
  <footer class="slide-footer">
    <svg class="band" width="458" height="21"><rect width="458" height="21" fill="var(--blue)"/><polygon points="361,0 458,0 458,21 353,21" fill="var(--blue-deep)"/><line x1="361" y1="0" x2="353" y2="21" stroke="#fff" stroke-width="1.2"/></svg>
    <span class="contact" style="left:24px"><i></i>+1 555 014 2290</span>
    <span class="contact" style="left:116px"><i></i>HELLO@GOODSHARBOR.CO</span>
    <span class="contact" style="left:236px"><i class="round"></i>WWW.GOODSHARBOR.CO</span>
    <span class="page-no">PAGE 04 OF 08</span>
  </footer>
</section>

<!-- Page 5 why -->
<section class="slide why col-r row1">
  <div class="slide-header">
    <svg width="458" height="30"><rect x="0" y="0" width="458" height="2" fill="var(--blue)"/><polygon points="0,0 294,0 277,29 0,29" fill="var(--blue)"/></svg>
    <div class="slide-title">WHY <b>GOODSHARBOR</b></div>
  </div>
  <div class="card" style="left:24px;top:82px;height:114px"><div class="icon"><svg width="20" height="20" viewBox="0 0 20 20"><ellipse cx="10" cy="9" rx="8" ry="6.5" fill="none" stroke="#fff" stroke-width="1.6"/><circle cx="6.5" cy="9" r="1.1" fill="#fff"/><circle cx="10" cy="9" r="1.1" fill="#fff"/><circle cx="13.5" cy="9" r="1.1" fill="#fff"/></svg></div><h3>HANDS ON SERVICE</h3><p style="top:36px">No automated portals or impersonal vendors, just dedicated partnership and personalized attention to your unique needs</p></div>
  <div class="card" style="left:129px;top:96px;height:114px"><div class="icon"><svg width="20" height="20" viewBox="0 0 20 20"><path d="M10 2l2.4 5 5.4.6-4 3.7 1.1 5.3L10 14l-4.9 2.6 1.1-5.3-4-3.7 5.4-.6z" fill="#fff"/></svg></div><h3>PREMIUM PRODUCT<br>ACCESS</h3><p class="two" style="top:46px">Curated selection of sustainable, trending and high-quality product lines that elevate your brand</p></div>
  <div class="card" style="left:234px;top:82px;height:114px"><div class="icon"><svg width="20" height="20" viewBox="0 0 20 20"><circle cx="10" cy="11" r="7" fill="none" stroke="#fff" stroke-width="1.6"/><path d="M10 7v4l2.5 2" stroke="#fff" stroke-width="1.6" fill="none"/><rect x="8" y="1.5" width="4" height="2" fill="#fff"/></svg></div><h3>FAST &amp; TRANSPARENT</h3><p style="top:36px">Quick turnaround times with clear, upfront pricing and no hidden fees or surprises</p></div>
  <div class="card" style="left:339px;top:96px;height:114px"><div class="icon"><svg width="20" height="20" viewBox="0 0 20 20"><circle cx="10" cy="10" r="7" fill="none" stroke="#fff" stroke-width="1.6"/><path d="M6.6 10.2l2.3 2.2 4.4-4.6" stroke="#fff" stroke-width="1.8" fill="none"/></svg></div><h3>PROVEN TRACK<br>RECORD</h3><p class="two" style="top:46px">Trusted experience working with Top 500 companies and national non-profit organizations</p></div>
  <footer class="slide-footer">
    <svg class="band" width="458" height="21"><rect width="458" height="21" fill="var(--blue)"/><polygon points="361,0 458,0 458,21 353,21" fill="var(--blue-deep)"/><line x1="361" y1="0" x2="353" y2="21" stroke="#fff" stroke-width="1.2"/></svg>
    <span class="contact" style="left:24px"><i></i>+1 555 014 2290</span>
    <span class="contact" style="left:116px"><i></i>HELLO@GOODSHARBOR.CO</span>
    <span class="contact" style="left:236px"><i class="round"></i>WWW.GOODSHARBOR.CO</span>
    <span class="page-no">PAGE 05 OF 08</span>
  </footer>
</section>

<!-- Page 6 industries -->
<section class="slide col-r row2">
  <div class="slide-header">
    <svg width="458" height="30"><rect x="0" y="0" width="458" height="2" fill="var(--blue)"/><polygon points="0,0 294,0 277,29 0,29" fill="var(--blue)"/></svg>
    <div class="slide-title">INDUSTRIES <b>WE SERVE</b></div>
  </div>
  <div class="pill" style="left:24px;top:38px"><div class="icon"><svg width="22" height="22" viewBox="0 0 22 22"><circle cx="11" cy="6" r="3" fill="#fff"/><circle cx="4.5" cy="8" r="2.3" fill="#fff"/><circle cx="17.5" cy="8" r="2.3" fill="#fff"/><path d="M4 18l4-5h6l4 5z" fill="#fff"/></svg></div><h4 style="top:8px">CORPORATE/EMPLOYEE ENGAGEMENT</h4><p style="top:19px">Strengthen company culture with branded merchandise and recognition programs</p></div>
  <div class="pill" style="left:235px;top:38px"><div class="icon"><svg width="22" height="22" viewBox="0 0 22 22"><rect x="3" y="4" width="16" height="15" rx="1.5" fill="none" stroke="#fff" stroke-width="1.6"/><line x1="3" y1="8" x2="19" y2="8" stroke="#fff" stroke-width="1.6"/><circle cx="11" cy="13.5" r="2.5" fill="#fff"/></svg></div><h4 style="top:14px">EVENTS &amp; CONFERENCES</h4><p style="top:25px">Memorable branded experiences and promotional items for attendees</p></div>
  <div class="pill" style="left:24px;top:105px"><div class="icon"><svg width="22" height="22" viewBox="0 0 22 22"><path d="M3 5h9v6a4.5 4.5 0 01-9 0z" fill="#fff"/><path d="M10 9h9v6a4.5 4.5 0 01-9 0z" fill="#fff" stroke="var(--blue)" stroke-width="1"/></svg></div><h4 style="top:8px">MUSIC &amp; ENTERTAINMENT</h4><p style="top:19px">Artist merchandise and fan engagement products that build lasting connections</p></div>
  <div class="pill" style="left:235px;top:105px"><div class="icon"><svg width="22" height="22" viewBox="0 0 22 22"><path d="M1 9l10-5 10 5-10 5z" fill="#fff"/><path d="M5 11v4c3 2.5 9 2.5 12 0v-4l-6 3z" fill="#fff"/></svg></div><h4 style="top:14px">EDUCATION &amp; ALUMNI RELATIONS</h4><p style="top:25px">School spirit products and alumni engagement merch</p></div>
  <div class="pill" style="left:24px;top:172px"><div class="icon"><svg width="22" height="22" viewBox="0 0 22 22"><path d="M8 6h6l-1 3c4 2 5 6 4 9H5c-1-3 0-7 4-9z" fill="#fff"/></svg></div><h4 style="top:8px">NON-PROFITS &amp; FUNDRAISERS</h4><p style="top:19px">Mission-driven merchandise that amplifies awareness and generates revenue</p></div>
  <div class="pill" style="left:235px;top:172px"><div class="icon"><svg width="22" height="22" viewBox="0 0 22 22"><path d="M4 3h8l7 7-8 9-7-7z" fill="#fff"/><circle cx="8" cy="7" r="1.4" fill="var(--blue)"/></svg></div><h4 style="top:14px">CONSUMER BRANDS</h4><p style="top:25px">Retail-quality branded products that extend your brand's reach</p></div>
  <footer class="slide-footer">
    <svg class="band" width="458" height="21"><rect width="458" height="21" fill="var(--blue)"/><polygon points="361,0 458,0 458,21 353,21" fill="var(--blue-deep)"/><line x1="361" y1="0" x2="353" y2="21" stroke="#fff" stroke-width="1.2"/></svg>
    <span class="contact" style="left:24px"><i></i>+1 555 014 2290</span>
    <span class="contact" style="left:116px"><i></i>HELLO@GOODSHARBOR.CO</span>
    <span class="contact" style="left:236px"><i class="round"></i>WWW.GOODSHARBOR.CO</span>
    <span class="page-no">PAGE 06 OF 08</span>
  </footer>
</section>

<!-- Page 7 interview -->
<section class="slide col-r row3">
  <h2 class="interview-title">LATEST MARGIN<br><b>MAGAZINE</b></h2>
  <div class="interview-rule"></div>
  <p class="interview-copy">Margin Magazine partnered with GoodsHarbor to design and produce stylish, brand-aligned merchandise that reflected the publication's creative and cultural influence. From limited-edition apparel and event giveaways to media collaborations, we delivered products that captured Margin's bold visual identity while meeting demanding timelines. The result was a curated collection that resonated with readers, artists, and advertisers - turning the magazine's distinct editorial voice into a tangible brand experience.</p>
  <div class="interview-photo" role="img" aria-label="Photo of a presenter showing a chart to a seated team in a bright office"></div>
  <div class="badge-ring"><span><svg width="16" height="16" viewBox="0 0 16 16"><circle cx="8" cy="8" r="5" fill="none" stroke="#fff" stroke-width="1.6"/><circle cx="8" cy="8" r="1.8" fill="#fff"/></svg></span></div>
</section>

<!-- Page 8 closing -->
<section class="slide closing col-r row4">
  <div class="closing-photo" role="img" aria-label="Photo of business people standing by tall office windows"></div>
  <div class="closing-band"></div>
  <div class="chat-badge"><svg width="16" height="16" viewBox="0 0 16 16"><ellipse cx="8" cy="7" rx="6" ry="4.5" fill="none" stroke="var(--blue)" stroke-width="1.6"/><path d="M5 11l-1 3 4-2.5" fill="var(--blue)"/></svg></div>
  <div class="closing-lead">WE LOOK FORWARD TO</div>
  <div class="closing-main">WORKING WITH YOU</div>
  <div class="closing-rule"></div>
  <div class="wordmark"><span class="dot"></span>GoodsHarbor</div>
</section>

</div>
</body>
</html>
```